Construction company focused on concrete and shed construction.

We need to update our current business card for brindlebuilds.com.au we would like an eye catching design with blue, grey and white incorporating our current logo.
Our company started off in concreting and due to varying factors we have expanded to include shed construction as well.
This has led to our current Logo looking a little out of place and somehow need to use the card to bring in the shed construction side of the business while not having to change current concrete look "BRINDLE" logo as we already have this incorporated into our company clothing and are not willing to change this yet.
Photo image attached for inspiration/ visual reference of type of work, not to be used on final design.
Please no cheesy designs of men in hard hats and tools
Final design should demonstrate a modern and service focused company.

Target Market(s)

Farmers, Business owners, Developers, Architects, Commercial project delivery

Industry/Entity Type

Construction Company

Contact Information for Business Card

Brindle Builds.
7c Harcourt st
Kelso Vale Tas
03 62918730

Font styles to use
Other font styles liked:
• see font in logo

Colors
3176b5
b2b2b2

Requirements
Must have
• Easy to read font,
• good contrast between back ground and writing
Nice to have
• Modern and corporate look with a fun but professional image.
Should not have
• Comic images or shadow images of tools/ people.

```html
<!DOCTYPE html>
<html lang="en">
<head>
<meta charset="utf-8">
<title>Brindle Group – Business Card</title>
<link href="https://fonts.googleapis.com/css2?family=Lato:wght@400;700;900&display=swap" rel="stylesheet">
<style>
  :root {
    --brand-blue: #3176b5;
    --brand-blue-deep: #1f5f9c;
    --brand-blue-light: #3b8cc4;
    --card-white: #ececec;
    --text-grey: #4a4a4a;
    --accent-grey: #b2b2b2;
    --stage: #d4d6d8;
  }
  * { box-sizing: border-box; margin: 0; padding: 0; }
  html, body { width: 1200px; height: 901px; overflow: hidden; }
  body {
    background: var(--stage);
    font-family: "Lato", sans-serif;
    display: flex;
    align-items: center;
    justify-content: center;
    gap: 40px;
  }
  .card {
    position: relative;
    width: 540px;
    height: 330px;
    border-radius: 22px;
    overflow: hidden;
    box-shadow: 0 6px 18px rgba(0,0,0,.18);
  }

  /* Front */
  .card-front {
    background: linear-gradient(135deg, var(--brand-blue-deep) 0%, var(--brand-blue) 55%, var(--brand-blue-light) 100%);
    display: flex;
    align-items: center;
    justify-content: center;
    gap: 16px;
  }
  .front-mark {
    width: 40px; height: 40px;
    border-radius: 50%;
    background: #f2f2f2;
  }
  .front-name {
    color: #f2f2f2;
    font-weight: 700;
    font-size: 34px;
    letter-spacing: 2px;
  }

  /* Back */
  .card-back { background: var(--card-white); }
  .back-logo {
    position: absolute;
    left: 40px; top: 34px;
    display: flex; align-items: center; gap: 10px;
  }
  .back-logo-mark {
    width: 26px; height: 26px;
    border-radius: 50%;
    background: var(--brand-blue);
  }
  .back-logo-name {
    color: var(--brand-blue);
    font-weight: 900;
    font-size: 22px;
    letter-spacing: 1px;
  }
  .paint-drips {
    position: absolute;
    right: 0; top: 0;
    width: 120px; height: 100%;
    background: linear-gradient(90deg, rgba(49,118,181,0) 0%, var(--brand-blue) 45%, var(--brand-blue-deep) 100%);
  }
  .contact {
    position: absolute;
    left: 40px; top: 100px;
    color: var(--text-grey);
    font-size: 15px;
    line-height: 1.35;
  }
  .person-name {
    color: var(--brand-blue);
    font-weight: 900;
    font-size: 22px;
    letter-spacing: .5px;
  }
  .person-role { font-size: 14px; margin-bottom: 8px; }
  .company {
    color: var(--brand-blue);
    font-weight: 900;
    font-size: 16px;
  }
  .address { margin-bottom: 8px; }
  .contact-line { display: flex; align-items: center; gap: 8px; }
  .contact-line svg { width: 14px; height: 14px; fill: var(--brand-blue-deep); flex: none; }
  .web strong { color: var(--brand-blue); font-weight: 900; }
</style>
</head>
<body>

  <section class="card card-front" aria-label="Card front">
    <span class="front-mark"></span>
    <span class="front-name">BRINDLE GROUP</span>
  </section>

  <section class="card card-back" aria-label="Card back">
    <div class="back-logo">
      <span class="back-logo-mark"></span>
      <span class="back-logo-name">BRINDLE</span>
    </div>

    <div class="paint-drips" role="img" aria-label="Blue paint drips running down the right edge"></div>

    <div class="contact">
      <p class="person-name">MARCUS TELFORD</p>
      <p class="person-role">Managing Director</p>
      <p class="company">BRINDLE GROUP</p>
      <p>7c Harcourt st</p>
      <p class="address">Kelso Vale Tas</p>
      <p class="contact-line">
        <svg viewBox="0 0 24 24" aria-hidden="true"><path d="M6.6 10.8a15.1 15.1 0 0 0 6.6 6.6l2.2-2.2a1 1 0 0 1 1-.25 11.4 11.4 0 0 0 3.6.57 1 1 0 0 1 1 1V20a1 1 0 0 1-1 1A17 17 0 0 1 3 4a1 1 0 0 1 1-1h3.5a1 1 0 0 1 1 1c0 1.25.2 2.45.57 3.57a1 1 0 0 1-.25 1z"/></svg>
        03 62918730
      </p>
      <p class="contact-line">
        <svg viewBox="0 0 24 24" aria-hidden="true"><path d="M6.6 10.8a15.1 15.1 0 0 0 6.6 6.6l2.2-2.2a1 1 0 0 1 1-.25 11.4 11.4 0 0 0 3.6.57 1 1 0 0 1 1 1V20a1 1 0 0 1-1 1A17 17 0 0 1 3 4a1 1 0 0 1 1-1h3.5a1 1 0 0 1 1 1c0 1.25.2 2.45.57 3.57a1 1 0 0 1-.25 1z"/></svg>
        1300 4 BRINDLE
      </p>
      <p class="contact-line">
        <svg viewBox="0 0 24 24" aria-hidden="true"><path d="M2 5h20v14H2z M2 5l10 8 10-8" /></svg>
        admin@brindlebuilds.com.au
      </p>
      <p class="contact-line web">
        <svg viewBox="0 0 24 24" aria-hidden="true"><circle cx="12" cy="12" r="10"/></svg>
        <span>www.<strong>brindlebuilds</strong>.com.au</span>
      </p>
    </div>
  </section>

</body>
</html>
```